card design for engineering consultancy

engineering drafting and project management company the provides drafting services for.
Electrical, Hydraulic, Mechanical, and Civil services
The company is called Q7R Services and logo is as attached
Information on card should be.
1. Logo
2.website : Q7RServices.example
3. email : info@Q7RServices.example
4. Phone: (+61) 400512836
5. Motto: Design - Document - Develop - Deliver

this card should be basically used for business identification only

Target Market(s)

electricians plumbers air conditioning installers and civil contractors

Industry/Entity Type

engineering, drafting, electrical, plumbing, airconditioning, civil

Contact Information for Business Card

1. Logo 2.website : Q7RServices.example 3. email : info@Q7RServices.example 4. Phone: (+61) 400512836 5. Motto: Design - Document - Develop - Deliver

Font styles to use
Serif

Requirements
Must have
• logo
Nice to have
• something inovative and different that makes it stand out from being just another business card

```html
<!DOCTYPE html>
<html lang="en">
<head>
<meta charset="utf-8">
<title>Q7R Services – Business Card</title>
<link rel="stylesheet" href="https://fonts.googleapis.com/css2?family=Cinzel:wght@600;700&family=Cormorant+SC:wght@500&display=swap">
<style>
  :root {
    --backdrop: #707376;
    --paper: #ffffff;
    --charcoal: #4a4a4c;
    --signal-red: #d0212f;
    --ink-soft: #555558;
  }
  * { margin: 0; padding: 0; box-sizing: border-box; }
  html, body {
    width: 1200px; height: 1200px; overflow: hidden;
    background: var(--backdrop);
  }
  .canvas { position: relative; width: 1200px; height: 1200px; }

  .card {
    position: absolute;
    width: 737px; height: 477px;
    background: var(--paper);
    box-shadow: 8px 9px 8px rgba(0,0,0,0.45);
    overflow: hidden;
  }
  .card--front { left: 87px; top: 86px; }
  .card--back  { left: 368px; top: 647px; }

  .wordmark {
    position: absolute; left: 0; right: 0;
    text-align: center;
    font-family: "Cinzel", serif;
    font-weight: 700;
    color: var(--charcoal);
    letter-spacing: 0.04em;
    white-space: nowrap;
  }
  .card--front .wordmark { top: 200px; font-size: 58px; }
  .card--back .wordmark  { top: 155px; font-size: 44px; }

  .motto {
    position: absolute; left: 0; right: 0; top: 52px;
    text-align: center;
    font-family: "Cinzel", serif;
    font-weight: 700;
    font-size: 23px;
    letter-spacing: 0.06em;
    color: var(--signal-red);
    padding-left: 52px;
    white-space: nowrap;
  }

  .contacts {
    position: absolute; left: 0; right: 0; top: 275px;
    list-style: none;
  }
  .contact {
    display: flex; justify-content: center; align-items: center;
    height: 39px;
    font-family: "Cormorant SC", serif;
    font-weight: 500;
    font-size: 20px;
    letter-spacing: 0.08em;
    color: var(--ink-soft);
  }
  .contact svg { width: 20px; height: 20px; margin-right: 14px; flex: none; }
  .contact--web   { padding-left: 12px; }
  .contact--phone { padding-left: 4px; }

  .accent-bar {
    position: absolute; left: 0; right: 0; bottom: 0; height: 14px;
    display: flex;
  }
  .accent-bar span { flex: 1; }
  .accent-bar .bar-charcoal { background: var(--charcoal); }
  .accent-bar .bar-red { background: var(--signal-red); }
</style>
</head>
<body>
<main class="canvas">

  <section class="card card--front" aria-label="Card front">
    <div class="wordmark">Q7R Services</div>
  </section>

  <section class="card card--back" aria-label="Card back">
    <p class="motto">Design - Document - Develop - Deliver</p>
    <div class="wordmark">Q7R Services</div>

    <ul class="contacts">
      <li class="contact contact--web">
        <svg viewBox="0 0 20 20" aria-hidden="true">
          <path d="M6 2 L9 5 L7.5 7.5 Q8.5 11 12 13 L14 11.5 L17 14.5 L15 17.5 Q9 18 5 12 Q2.5 7 6 2 Z" fill="var(--signal-red)"/>
        </svg>
        Q7RServices.example
      </li>
      <li class="contact contact--email">
        <svg viewBox="0 0 22 16" aria-hidden="true" style="width:24px;height:18px">
          <rect x="0" y="0" width="22" height="16" fill="var(--signal-red)"/>
          <path d="M1 1 L11 9 L21 1 M1 15 L8 7.5 M21 15 L14 7.5" stroke="#fff" stroke-width="1.4" fill="none"/>
        </svg>
        info@Q7RServices.example
      </li>
      <li class="contact contact--phone">
        <svg viewBox="0 0 20 20" aria-hidden="true">
          <circle cx="10" cy="10" r="8.5" fill="none" stroke="var(--signal-red)" stroke-width="2"/>
          <path d="M1.5 10 H18.5 M10 1.5 V18.5 M3.5 5.5 H16.5 M3.5 14.5 H16.5" stroke="var(--signal-red)" stroke-width="1.5"/>
          <path d="M12 11 L19 14 L16 15 L18.5 18 L17 19 L14.5 16 L13 19 Z" fill="var(--signal-red)" stroke="#fff" stroke-width="0.8"/>
        </svg>
        (+61) 400512836
      </li>
    </ul>

    <div class="accent-bar" aria-hidden="true">
      <span class="bar-charcoal"></span><span class="bar-red"></span>
    </div>
  </section>

</main>
</body>
</html>
```